New Business Card Design for Engineering and Surveying Company

We need a new design template for our business cards. We are a civil engineering, land surveying and pipeline integrity business. Please see dkhpartners.com for details. We need a bold, new business card design to complement our rebranding and marketing program. We have anew logo and attached vectro file. Please find additional details below. I am available to answer any questions.

Target Market(s)

Contractors, business owners, oil companies

Contact Information for Business Card

Needs to be customizable for different people (name, title, cell)

Font styles to use
Sans Serif
Other font styles liked:
• See eps file

Requirements
Must have
• Example Information:
Trevor Ashcombe

T:409-555-0173
M: 202-555-0148
tashcombe@dkhprtnrs.com

Address: 1875 Pinecrest Parkway, Beaumont, Texas 77703
Email: tolvanrey@dkhpartners.com
Website: www.dkhpartners.com
Nice to have
• I would like the back of the card to have the logo on a bold background with the text below:

[logo]
DORAN KESSLING & PARTNERS
CIVIL ENGINEERING | LAND SURVEYING | PIPELINE INTEGRITY

The reverse side should have the contact information for the person (example above), a smaller version of the logo and a graphic

```html
<!DOCTYPE html>
<html lang="en">
<head>
<meta charset="utf-8">
<title>Doran Kessling &amp; Partners — Business Card</title>
<link href="https://fonts.googleapis.com/css2?family=Montserrat:wght@500;700&display=swap" rel="stylesheet">
<style>
  :root {
    --brand-blue: #224e9e;
    --brand-red: #e52330;
    --ink: #111111;
    --card-back: #000000;
    --paper: #ffffff;
    --edge: #222222;
  }
  html, body {
    margin: 0;
    padding: 0;
    width: 1200px;
    height: 1200px;
    overflow: hidden;
    background: var(--paper);
    font-family: "Montserrat", Arial, sans-serif;
  }
  .canvas {
    position: relative;
    width: 1200px;
    height: 1200px;
  }
  .card {
    position: absolute;
    top: 441px;
    width: 556px;
    height: 318px;
    border-radius: 37px;
    overflow: hidden;
    box-sizing: border-box;
  }
  .card--front {
    left: 41px;
    background: var(--paper);
    border: 1px solid var(--edge);
  }
  .card--back {
    left: 603px;
    background: var(--card-back);
  }
  .corner-band {
    position: absolute;
    display: block;
  }
  .card--front .corner-band { left: 0; bottom: 0; }
  .card--back .corner-band { right: 0; top: 0; }

  .brand-name {
    position: absolute;
    margin: 0;
    font-weight: 700;
    letter-spacing: 0.02em;
    line-height: 1.05;
  }
  .card--front .brand-name {
    left: 52px;
    top: 48px;
    font-size: 22px;
    color: var(--brand-blue);
  }
  .contact {
    position: absolute;
    left: 86px;
    top: 136px;
    margin: 0;
    font-size: 15px;
    font-weight: 500;
    color: var(--ink);
    line-height: 19px;
  }
  .contact .label { display: inline-block; width: 33px; }
  .contact .gap { height: 8px; }
  .person {
    position: absolute;
    left: 334px;
    top: 109px;
    color: var(--ink);
  }
  .person__name {
    margin: 0;
    font-size: 16px;
    font-weight: 700;
    padding-bottom: 1px;
    border-bottom: 2px solid var(--ink);
    display: inline-block;
  }
  .person__title {
    margin: 2px 0 0;
    font-size: 15px;
    font-weight: 500;
  }
  .address {
    position: absolute;
    left: 0;
    width: 556px;
    top: 259px;
    margin: 0;
    text-align: center;
    font-size: 15px;
    font-weight: 500;
    line-height: 20px;
    color: var(--ink);
    font-style: normal;
  }

  .card--back .brand-name {
    left: 0;
    width: 556px;
    top: 112px;
    text-align: center;
    font-size: 40px;
    color: var(--paper);
  }
  .services {
    position: absolute;
    left: 0;
    width: 556px;
    top: 255px;
    margin: 0;
    text-align: center;
    font-size: 14px;
    font-weight: 700;
    color: var(--paper);
    letter-spacing: 0.01em;
  }
</style>
</head>
<body>
<main class="canvas">

  <section class="card card--front" aria-label="Business card front">
    <p class="brand-name">DORAN KESSLING<br>&amp; PARTNERS</p>

    <div class="person">
      <p class="person__name">Trevor Ashcombe</p>
      <p class="person__title">CEO</p>
    </div>

    <div class="contact">
      <div><span class="label">T :</span>409-555-0173</div>
      <div><span class="label">M :</span>202-555-0148</div>
      <div class="gap"></div>
      <div>tolvanrey@dkhpartners.com</div>
      <div>www.dkhpartners.com</div>
    </div>

    <address class="address">1875 Pinecrest Parkway,<br>Beaumont, Texas 77703</address>

    <svg class="corner-band" width="120" height="52" viewBox="0 0 120 52" aria-hidden="true">
      <polygon points="0,0 118,52 0,52" fill="var(--brand-blue)"/>
    </svg>
  </section>

  <section class="card card--back" aria-label="Business card back">
    <svg class="corner-band" width="120" height="52" viewBox="0 0 120 52" aria-hidden="true">
      <polygon points="2,0 120,0 120,51" fill="var(--brand-blue)"/>
    </svg>

    <p class="brand-name">DORAN KESSLING<br>&amp; PARTNERS</p>

    <p class="services">CIVIL ENGINEERING | LAND SURVEYING | PIPELINE INTEGRITY</p>
  </section>

</main>
</body>
</html>
```